Ad For Home Magazine for Landscape Architecture company

Hi Designers,

We are a dedicated landscape architecture and outdoor construction company. We need a little help with an ad design for a magazine.

Our approach should be elegant but accessible. Our clientele is high end.

visit our site to get to know us and get our style: www.brivolane.com

The focus of this ad will be in Outdoor living spaces | custom outdoor kitchens and premium outdoor kitchen appliances. as such the images chosen should showcase all of these.

Ad Specs: Full Page, see attachment.

Images: 1-4 images total for the ad. choose from pictures upload

Logo: Orginal Logo and logo variation included.

Showroom section: (optional) images for the showroom are included. this section is optional and up to the designer.

Text 1: Outdoor Living Spaces| Custom Outdoor Kitchens | Premium Appliances
Text 2 ( Company info) 305.862.3094 | Brivolane.com | 4418 NW 62 AVE, Doral FL 33166

Target Market(s)

High end

Industry/Entity Type

Architecture

Font styles to use
Serif
Sans Serif

Colors

Designer to choose colors to be used in the design.

Requirements
Must have
• Text:
• - Custom Outdoor Living Spaces | Outdoor Kitchens | Appliances
• - Company Info
• - Logo
• - Pictures (1-4)
Nice to have
• A showroom section or picture - only if the design works
Should not have
• Any

```html
<!DOCTYPE html>
<html lang="en">
<head>
<meta charset="utf-8">
<title>Brivolane – Outdoor Living Spaces Ad</title>
<link rel="stylesheet" href="https://fonts.googleapis.com/css2?family=Montserrat:wght@400;800&family=Roboto+Condensed:wght@300;400;700&display=swap">
<style>
  :root {
    --backdrop: #9d99a6;
    --paper: #ffffff;
    --green-deep: #1f7a3c;
    --green-mid: #3a9a3e;
    --green-lime: #8cc63f;
    --charcoal: #2b2b2d;
    --text-light: #ffffff;
  }
  html, body {
    margin: 0;
    width: 1155px;
    height: 1200px;
    overflow: hidden;
    background: var(--backdrop);
  }
  .ad-page {
    position: absolute;
    left: 172px;
    top: 40px;
    width: 810px;
    height: 1120px;
    display: block;
  }
  .brand-name { font-family: "Montserrat", sans-serif; font-weight: 400; fill: var(--green-deep); }
  .headline { font-family: "Montserrat", sans-serif; font-weight: 800; }
  .subline { font-family: "Montserrat", sans-serif; font-weight: 400; }
  .condensed { font-family: "Roboto Condensed", sans-serif; }
</style>
</head>
<body>
<svg class="ad-page" viewBox="0 0 618 855" preserveAspectRatio="none" xmlns="http://www.w3.org/2000/svg">
  <defs>
    <linearGradient id="heroTone" x1="0" y1="0" x2="0" y2="1">
      <stop offset="0" stop-color="#d9e4ea"/>
      <stop offset="0.35" stop-color="#4e5a55"/>
      <stop offset="0.6" stop-color="#c3ccd3"/>
      <stop offset="1" stop-color="#9fb0c0"/>
    </linearGradient>
    <linearGradient id="poolTone" x1="0" y1="0" x2="1" y2="1">
      <stop offset="0" stop-color="#5d6a70"/>
      <stop offset="0.5" stop-color="#b9c4cc"/>
      <stop offset="1" stop-color="#3f6f9a"/>
    </linearGradient>
    <linearGradient id="limeFade" x1="0" y1="0" x2="1" y2="0">
      <stop offset="0" stop-color="#3a9a3e" stop-opacity="0.85"/>
      <stop offset="1" stop-color="#8cc63f"/>
    </linearGradient>
    <linearGradient id="bannerGreen" x1="0" y1="0" x2="1" y2="0">
      <stop offset="0" stop-color="#8cc63f"/>
      <stop offset="1" stop-color="#2f8a3b"/>
    </linearGradient>
    <linearGradient id="darkBox" x1="0" y1="0" x2="1" y2="1">
      <stop offset="0" stop-color="#3a3a3c"/>
      <stop offset="1" stop-color="#1e1e20"/>
    </linearGradient>
  </defs>

  <rect class="page-paper" width="618" height="855" fill="var(--paper)"/>

  <g class="brand">
    <circle cx="50" cy="89" r="6" fill="var(--green-deep)"/>
    <text class="brand-name" x="63" y="96" font-size="19" letter-spacing="1">BRIVOLANE</text>
  </g>

  <polygon role="img" aria-label="Photo: pergola-covered patio with bar seating and lounge furniture beside a pool"
    points="260,0 618,0 618,390 140,390" fill="url(#heroTone)"/>
  <polygon points="600,0 618,0 618,390 500,390" fill="url(#limeFade)" opacity="0.85"/>

  <polygon points="23,182 185,182 23,730" fill="var(--green-deep)"/>

  <polygon points="135,402 482,402 448,513 100,513" fill="url(#bannerGreen)"/>
  <text class="headline" x="292" y="463" font-size="50" fill="var(--text-light)" text-anchor="middle">OUTDOOR</text>
  <line x1="150" y1="470" x2="436" y2="470" stroke="var(--text-light)" stroke-width="1"/>
  <text class="subline" x="292" y="494" font-size="21" letter-spacing="6" fill="var(--text-light)" text-anchor="middle">LIVING SPACES</text>

  <polygon role="img" aria-label="Photo: outdoor kitchen pavilion beside a round pool with palm trees"
    points="492,402 618,402 618,513 460,513" fill="url(#poolTone)"/>

  <polygon role="img" aria-label="Photo: covered lounge area with ceiling fan overlooking a pool"
    points="95,525 265,525 235,635 63,635" fill="url(#poolTone)"/>
  <polygon role="img" aria-label="Photo: modern home with long pool and sun loungers"
    points="280,525 450,525 420,635 248,635" fill="url(#heroTone)"/>

  <polygon points="463,525 618,525 618,635 433,635" fill="url(#darkBox)"/>
  <text class="condensed" x="605" y="570" font-size="15" font-weight="300" fill="var(--text-light)" text-anchor="end">GET IN TOUCH</text>
  <line x1="510" y1="575" x2="605" y2="575" stroke="var(--text-light)" stroke-width="0.8"/>
  <text class="condensed" x="605" y="598" font-size="21" font-weight="700" fill="var(--green-lime)" text-anchor="end">305.862.3094</text>

  <text class="headline" x="68" y="720" font-size="55" fill="var(--green-mid)">CUSTOM</text>
  <text class="subline" x="71" y="746" font-size="23" fill="var(--green-mid)">OUTDOOR KITCHENS</text>

  <polygon points="445,650 618,650 618,855 365,855" fill="var(--green-deep)"/>
  <text class="condensed" x="605" y="695" font-size="17" font-weight="700" fill="var(--text-light)" text-anchor="end">CONTACT US</text>
  <line x1="502" y1="702" x2="618" y2="702" stroke="var(--text-light)" stroke-width="0.8"/>
  <g class="contact-icons" fill="var(--text-light)">
    <path d="M576 718 a6 6 0 0 1 6 6 c0 5 -6 11 -6 11 s-6 -6 -6 -11 a6 6 0 0 1 6 -6z"/>
    <circle cx="576" cy="724" r="2.2" fill="var(--green-deep)"/>
    <circle cx="595" cy="726" r="7"/>
  </g>
  <text class="condensed" x="605" y="762" font-size="15" font-weight="300" fill="var(--text-light)" text-anchor="end">4418 NW 62 AVE,</text>
  <text class="condensed" x="605" y="784" font-size="15" font-weight="300" fill="var(--text-light)" text-anchor="end">Doral FL 33166</text>
  <text class="condensed" x="605" y="815" font-size="15" font-weight="300" fill="var(--text-light)" text-anchor="end">www.Brivolane.com</text>

  <polygon points="23,770 378,770 355,855 23,855" fill="url(#bannerGreen)"/>
  <text class="condensed" x="60" y="825" font-size="33" font-weight="400" fill="var(--text-light)" textLength="280" lengthAdjust="spacingAndGlyphs">PREMIUM APPLIANCES</text>
</svg>
</body>
</html>
```